Website for Law Firm in California with Existing Logo (Pagewright)

I need a website for a law firm based in Orange County, California, called "Hollis Legal Group." The firm will provide civil litigation and business advice services. The principal practice areas include business litigation, real estate litigation, construction litigation, and other general commercial litigation.

I practiced at a very large, international law firm for 10 years (Merrow Tash LLP) before starting Hollis Legal Group.

At the moment, Hollis Legal Group has one attorney, Corwin J. Hollis (me).

I have a logo for Hollis Legal Group (see attached files, including vectors and transparent background)--which is dark blue and gray. I am open to color changes/tweaks, but would prefer designs that communicate dependability, competence, sophistication, and trustworthiness.

The site should include a home page, as well as separate pages containing: (1) information about the firm and Corwin Hollis (e.g., "About"); (2) information about the firm's practice areas (use "Practice Areas"); (3) a "Contact Us" page where the visitor can insert contact information and describe their legal problem or help sought; (4) a page for articles and blog posts.

I'd also like to mention the practice areas on the main page with links to pages dedicated to each practice area. My thought is that these "practice areas" pages will have a similar look and design, but I will, of course, alter the content for each one.

The practice areas to list for now (I may add more or remove some later are):

Business Litigation
Real Estate Litigation
Banking & Lending Litigation
Contract Disputes
Construction Litigation
Commercial Litigation
Fraud Claims
Breach of Fiduciary Claims
Creditor's Rights
Judgment Collection
Appellate Law
Consumer and Personal Injury Claims
ADA Disputes
Other Civil Litigation
General Corporate Advice
Contract Review
Business Entity Formation

Each page should include easily viewable contact information without appearing cheesy.

I uploaded some head shots and photos of my building as well. They need not all be used. Feel free to play with adjustments to the photos (B&W, contrast, etc.).

I own and reserve the copyright to all files, logos, and pictures uploaded with this design.

I will provide a description of the firm and Corwin Hollis for the about page, as well as a summary of each practice area for the practice area page.

I will also need the ability to put a small description of the localities served by the firm at the bottom of each page on the site, along with a website disclaimer about representations made (I will provide the language for this too).

I am contemplating creating additional websites for different practice areas as well. So this may grow into a larger project if your design is selected. I will likely want to link to those sites from my home site if it makes sense to do so.

Thank you.

Reason: I was involved in a car incident yesterday and need a few more days to review designs. Thanks.

Target Market(s)

Legal Services for businesses and business owners, also individuals.

Industry/Entity Type

Attorney

Contact Information for Business Card

Please include my name and the title "Managing Attorney." Please include fields for my address, telephone number, and email address. Also please include "Orange County" and "Los Angeles" on the card.

Font styles to use
Sans Serif

Requirements
Must have
• See description
Nice to have
• See description
Should not have
• See description

```html
<!DOCTYPE html>
<html lang="en">
<head>
<meta charset="utf-8">
<title>Hollis Legal Group</title>
<link rel="stylesheet" href="https://fonts.googleapis.com/css2?family=Cinzel:wght@400;600&family=Arimo:wght@400&family=Open+Sans:ital,wght@1,600;1,700&display=swap">
<style>
  :root {
    --navy: #1b2d66;
    --navy-deep: #0e1838;
    --sky-top: #2f5db0;
    --sky-bottom: #7fa9dc;
    --steel: #6fa3bd;
    --ink: #333a45;
    --muted: #6b6f76;
    --heading-grey: #5d6577;
    --white: #ffffff;
    --field-text: #9a9ea5;
    --hover-grey: #8a90a0;
  }
  * { box-sizing: border-box; margin: 0; padding: 0; }
  html, body { width: 1200px; height: 2655px; overflow: hidden; background: var(--white); }
  body { font-family: "Arimo", Arial, sans-serif; color: var(--ink); }
  .page { position: relative; width: 1200px; height: 2655px; }

  /* Hero */
  .hero { position: absolute; left: 0; top: 0; width: 1200px; height: 752px; overflow: hidden; }
  .hero-photo { position: absolute; inset: 0;
    background: linear-gradient(160deg, var(--sky-top) 0%, #4c7fc8 45%, var(--sky-bottom) 100%); }
  .hero-photo::after { content: ""; position: absolute; inset: 0;
    background: linear-gradient(90deg, rgba(20,35,80,.35) 0%, rgba(20,35,80,0) 55%); }

  .site-header { position: absolute; left: 0; top: 0; width: 1200px; height: 103px;
    background: rgba(25, 48, 110, .78); }
  .brand { position: absolute; left: 67px; top: 31px; font-family: "Cinzel", serif;
    font-weight: 400; font-size: 32px; letter-spacing: 1px; color: var(--white); white-space: nowrap; }
  .main-nav { position: absolute; top: 52px; left: 0; width: 1200px; height: 24px; }
  .main-nav a { position: absolute; top: 0; font-family: "Cinzel", serif; font-size: 16px;
    letter-spacing: 1px; color: rgba(255,255,255,.82); text-decoration: none; white-space: nowrap;
    transform: translateY(-50%); line-height: 1; }
  .main-nav a.is-current { color: var(--white); }
  .main-nav a.is-current::after { content: ""; position: absolute; left: -2px; right: -2px; top: 32px;
    height: 4px; background: var(--white); }
  .nav-sep { position: absolute; top: -11px; width: 1px; height: 22px; background: rgba(255,255,255,.7); }

  .hero-title { position: absolute; left: 67px; top: 244px; width: 520px; font-family: "Cinzel", serif;
    font-weight: 400; font-size: 35px; line-height: 42px; letter-spacing: 1px; color: var(--white); text-transform: uppercase; }
  .hero-text { position: absolute; left: 70px; top: 398px; width: 480px; font-size: 16.5px;
    line-height: 21px; color: var(--white); }
  .btn { display: block; background: var(--navy); color: var(--white); font-family: "Cinzel", serif;
    text-align: center; text-transform: uppercase; letter-spacing: 1px; text-decoration: none; }
  .hero-btn { position: absolute; left: 74px; top: 616px; width: 223px; height: 37px; line-height: 37px; font-size: 16px; }

  /* Intro */
  .intro { position: absolute; left: 0; top: 752px; width: 1200px; height: 335px; text-align: center; }
  .intro-title { margin-top: 76px; font-family: "Cinzel", serif; font-weight: 400; font-size: 30px;
    letter-spacing: 1.5px; color: var(--heading-grey); }
  .intro-sub { margin-top: 6px; font-size: 22px; color: var(--ink); }
  .intro-text { width: 690px; margin: 10px auto 0; font-size: 16.5px; line-height: 21px; color: var(--muted); }

  /* Attorney */
  .attorney { position: absolute; left: 0; top: 1087px; width: 1200px; height: 400px; }
  .attorney-photo { position: absolute; left: 0; top: 0; width: 600px; height: 400px;
    background: linear-gradient(180deg, #b9c2c6 0%, #d7dbd9 50%, #8e9699 100%); }
  .attorney-panel { position: absolute; left: 600px; top: 0; width: 600px; height: 400px; background: var(--steel); }
  .quote-block { position: absolute; left: 143px; top: 140px; width: 345px; }
  .quote { font-family: "Open Sans", sans-serif; font-style: italic; font-weight: 600;
    font-size: 16.5px; line-height: 21px; letter-spacing: -0.1px; color: var(--white); }
  .quote-name { margin-top: 16px; margin-left: 2px; font-family: "Cinzel", serif; font-size: 16px;
    letter-spacing: 1px; color: var(--white); }

  /* Practice areas */
  .practice { position: absolute; left: 0; top: 1487px; width: 1200px; height: 366px;
    background: linear-gradient(180deg, #16224a 0%, var(--navy-deep) 100%); }
  .practice-photo { position: absolute; inset: 0; opacity: .45;
    background: linear-gradient(90deg, #2c3550 0%, #1a2440 40%, #2a3250 70%, #141c36 100%); }
  .practice-title { position: absolute; left: 0; top: 54px; width: 1200px; text-align: center;
    font-family: "Cinzel", serif; font-weight: 400; font-size: 26px; letter-spacing: 1px; color: var(--white); }
  .practice-rule { position: absolute; left: 464px; top: 106px; width: 264px; height: 1px; background: rgba(255,255,255,.75); }
  .practice-list { position: absolute; top: 132px; list-style: none; }
  .practice-list li { font-size: 16.5px; line-height: 21px; }
  .practice-list a { color: var(--white); text-decoration: none; }
  .practice-list a.is-hover { color: var(--hover-grey); }
  .list-left { left: 223px; }
  .list-right { left: 766px; }

  /* Contact */
  .contact { position: absolute; left: 0; top: 1853px; width: 1200px; height: 802px; overflow: hidden; }
  .contact-photo { position: absolute; inset: 0;
    background: linear-gradient(180deg, #7fb2e0 0%, #9cb9cf 30%, #8b949a 60%, #5d6c5a 85%, #2d3d2a 100%); }
  .contact-intro { position: absolute; left: 354px; top: 138px; width: 496px; height: 160px;
    background: rgba(90,110,135,.35); }
  .contact-intro p { position: absolute; left: 32px; top: 8px; width: 432px; text-align: center;
    font-size: 16.5px; line-height: 21px; color: var(--white); }
  .contact-heading { position: absolute; left: 0; top: 368px; width: 1200px; text-align: center;
    font-size: 22px; font-weight: 400; color: var(--white); }
  .contact-form { position: absolute; left: 437px; top: 425px; width: 324px; }
  .field { display: block; width: 324px; height: 35px; margin-bottom: 2px; border: 0; background: var(--white);
    padding: 0 10px; font-family: "Arimo", Arial, sans-serif; font-size: 14px; color: var(--ink); }
  .field::placeholder { color: var(--field-text); }
  textarea.field { height: 88px; padding-top: 8px; resize: none; }
  .send-btn { position: absolute; left: 48px; top: 228px; width: 223px; height: 39px; border: 0;
    line-height: 39px; font-size: 16px; cursor: pointer; }
  .copyright { position: absolute; left: 0; top: 752px; width: 1200px; text-align: center;
    font-family: "Cinzel", serif; font-size: 15px; letter-spacing: 1px; color: var(--white); }
</style>
</head>
<body>
<div class="page">

  <section class="hero">
    <div class="hero-photo" role="img" aria-label="Photo looking up at a glass office tower and palm trees against a blue sky"></div>

    <header class="site-header">
      <div class="brand">Hollis Legal Group</div>
      <nav class="main-nav">
        <a class="is-current" href="#" style="left:469px">Home</a>
        <span class="nav-sep" style="left:552px"></span>
        <a href="#" style="left:579px">About</a>
        <span class="nav-sep" style="left:672px"></span>
        <a href="#" style="left:704px">Practice Areas</a>
        <span class="nav-sep" style="left:881px"></span>
        <a href="#" style="left:911px">Contact Us</a>
        <span class="nav-sep" style="left:1060px"></span>
        <a href="#" style="left:1092px">Blog</a>
      </nav>
    </header>

    <h1 class="hero-title">Lorem ipsum dolor sit amet, graeci phaedrum elaboraret at vel.</h1>
    <p class="hero-text">Lorem ipsum dolor sit amet, graeci phaedrum elaboraret at vel. Pro ex vitae senserit. Stet aeterno est te. Congue disputationi comprehensam usu in, duo ne quidam dictas adipisci</p>
    <a class="btn hero-btn" href="#">Contact me today</a>
  </section>

  <section class="intro">
    <h2 class="intro-title">Hollis Legal Group</h2>
    <p class="intro-sub">Civil litigation and business advice services</p>
    <p class="intro-text">The principal practice areas include business litigation, real estate litigation, construction litigation, and other general commercial litigation. Lorem ipsum dolor sit amet, graeci phaedrum elaboraret at vel. Pro ex vitae senserit. Stet aeterno est te. Congue disputationi comprehensam usu in, duo ne quidam dictas adipisci</p>
  </section>

  <section class="attorney">
    <div class="attorney-photo" role="img" aria-label="Portrait of the managing attorney standing at the glass entrance of the office building"></div>
    <div class="attorney-panel">
      <div class="quote-block">
        <blockquote class="quote">“Lorem ipsum dolor sit amet, graeci phaedrum elaboraret at vel. Pro ex vitae senserit. Stet aeterno est te. Congue disputationi comprehensam usu in, duo ne quidam dictas adipisci”</blockquote>
        <p class="quote-name">Corwin J. Hollis</p>
      </div>
    </div>
  </section>

  <section class="practice">
    <div class="practice-photo" role="img" aria-label="Darkened photo of business people meeting in an office"></div>
    <h2 class="practice-title">Practice Areas</h2>
    <div class="practice-rule"></div>
    <ul class="practice-list list-left">
      <li><a href="#">Business Litigation</a></li>
      <li><a href="#">Real Estate Litigation</a></li>
      <li><a href="#">Banking &amp; Lending Litigation</a></li>
      <li><a href="#">Contract Disputes</a></li>
      <li><a class="is-hover" href="#">Construction Litigation</a></li>
      <li><a href="#">Commercial Litigation</a></li>
      <li><a href="#">Fraud Claims</a></li>
      <li><a href="#">Breach of Fiduciary Claims</a></li>
    </ul>
    <ul class="practice-list list-right">
      <li><a href="#">Creditor's Rights</a></li>
      <li><a href="#">Judgment Collection</a></li>
      <li><a href="#">Appellate Law</a></li>
      <li><a href="#">Consumer and Personal Injury Claims</a></li>
      <li><a href="#">ADA Disputes</a></li>
      <li><a href="#">Other Civil Litigation</a></li>
      <li><a href="#">General Corporate Advice</a></li>
      <li><a href="#">Contract Review</a></li>
      <li><a href="#">Business Entity Formation</a></li>
    </ul>
  </section>

  <section class="contact">
    <div class="contact-photo" role="img" aria-label="Photo of the office building entrance lined with palm trees and landscaped plants"></div>
    <div class="contact-intro">
      <p>Lorem ipsum dolor sit amet, graeci phaedrum elaboraret at vel. Pro ex vitae senserit. Stet aeterno est te. Congue disputationi comprehensam usu in, duo ne quidam dictas adipisci, te duis ubique dicunt quo, pro ut assentior percipitur repudiandae.</p>
    </div>
    <h2 class="contact-heading">Get in touch today and let's discuss your options!</h2>
    <form class="contact-form">
      <input class="field" type="text" placeholder="Full Name">
      <input class="field" type="email" placeholder="Email">
      <input class="field" type="tel" placeholder="Phone">
      <textarea class="field" placeholder="Message"></textarea>
      <button class="btn send-btn" type="submit">Send</button>
    </form>
    <p class="copyright">Copyright © 2016 HollisLegalGroup</p>
  </section>

</div>
</body>
</html>
```